I need a business card design for my new clinic (SPORTS MEDICINE OF KNEE). I am orthopedist, expert in sports surgery, especially knee surgery. I prefer, as colors, the colors of my logo (green, black and white). I already have my logo and should appear on my card. It's good to see my site to have ideas (www.drlucianovarela.com)
It needs contain:
my name: Dr. Luciano Varela
my registration: CRM 584-902
my specialty: Cirurgia do Joelho / Esporte
my address: Centro Executivo - Pinheiral Plaza
Av. Doutor Augusto Brandão Cunha, 2740 sala 0836
Jd. Ipanema - Ribeirão Preto - SP
my phone number: Tel (16) 8245-3908
my clinic phone: (16) 3670-4851
my e-mail: drlucianovarela@mailbox-exemplo.com
my site: www.drlucianovarela.com

Target Market(s)

futures patients

Industry/Entity Type

Clinic

Requirements
Nice to have
• letters not overfilled
straight lines, with few curves

```html
<!DOCTYPE html>
<html lang="pt-BR">
<head>
<meta charset="utf-8">
<title>Cartão de visita — Dr. Luciano Varela</title>
<link rel="stylesheet" href="https://fonts.googleapis.com/css2?family=Tinos:wght@400;700&display=swap">
<style>
  :root {
    --page-bg: #ece7df;
    --card-black: #000000;
    --card-white: #ffffff;
    --brand-green: #3fae6e;
    --art-green: #1f5a1c;
    --ink: #111111;
    --ink-soft: #222222;
    --paper-text: #f2f2f2;
  }
  * { margin: 0; padding: 0; box-sizing: border-box; }
  html, body {
    width: 1200px; height: 1000px; overflow: hidden;
    background: var(--page-bg);
    font-family: "Tinos", "Times New Roman", serif;
  }
  .canvas { position: relative; width: 1200px; height: 1000px; }

  .card {
    position: absolute; top: 203px; width: 350px; height: 594px; overflow: hidden;
    box-shadow: 0 2px 6px rgba(0,0,0,.25);
  }
  .card--front { left: 237px; background: var(--card-black); }
  .card--back { left: 612px; background: var(--card-white); color: var(--ink); text-align: center; }

  .art-area {
    position: absolute; left: 100px; top: 0; width: 250px; height: 594px;
    background: linear-gradient(90deg, var(--card-black) 0%, var(--art-green) 100%);
  }

  .brand { position: absolute; display: flex; align-items: center; }
  .brand__square { width: 60px; height: 58px; background: var(--brand-green); border-radius: 6px; flex: none; }
  .brand__name { font-weight: 400; font-size: 46px; letter-spacing: 1px; line-height: 1; margin-left: 12px; }
  .card--front .brand { left: 27px; top: 44px; }
  .card--front .brand__name { color: var(--paper-text); }
  .card--back .brand { left: 66px; top: 54px; }
  .card--back .brand__name { color: var(--ink); font-size: 41px; margin-left: 11px; }

  .website {
    position: absolute; left: 71px; top: 542px;
    color: var(--paper-text); font-size: 15px;
  }

  .doctor { position: absolute; left: 0; right: 0; top: 257px; }
  .doctor__name { font-size: 20px; font-weight: 700; }
  .doctor__crm { font-size: 16px; font-weight: 700; margin-top: 6px; }
  .doctor__specialty { font-size: 12.5px; margin-top: 12px; color: var(--ink-soft); }
  .doctor__phone { font-size: 12.5px; margin-top: 6px; color: var(--ink-soft); }

  .address {
    position: absolute; left: 0; right: 0; top: 446px;
    font-size: 13px; font-weight: 700; line-height: 16px; font-style: normal;
  }
  .contact { position: absolute; left: 0; right: 0; top: 527px; font-size: 13px; font-weight: 700; }
  .contact__phone { margin-top: 12px; }
</style>
</head>
<body>
<main class="canvas">
  <section class="card card--front">
    <div class="art-area" role="img" aria-label="Ilustração em raio-x verde de uma articulação do joelho sobre fundo preto"></div>
    <div class="brand">
      <span class="brand__square"></span>
      <span class="brand__name">VARELA</span>
    </div>
    <p class="website">www.drlucianovarela.com</p>
  </section>

  <section class="card card--back">
    <div class="brand">
      <span class="brand__square"></span>
      <span class="brand__name">VARELA</span>
    </div>
    <div class="doctor">
      <h1 class="doctor__name">Dr. Luciano Varela</h1>
      <p class="doctor__crm">CRM 584-902</p>
      <p class="doctor__specialty">Cirurgia do Joelho / Esporte</p>
      <p class="doctor__phone">(16) 8245-3908</p>
    </div>
    <address class="address">
      Centro Executivo - Pinheiral Plaza<br>
      Av. Doutor Augusto Brandão Cunha,<br>
      2740 sala 0836 Jd. Ipanema<br>
      Ribeirão Preto - SP
    </address>
    <div class="contact">
      <p class="contact__email">drlucianovarela@mailbox-exemplo.com</p>
      <p class="contact__phone">(16) 3670-4851</p>
    </div>
  </section>
</main>
</body>
</html>
```